Commercial Loan Originator Business Card (CHANGE COLORS SCHEME)

CHANGE COLOR SCHEME - SAME DESIGN

Name Marissa Lantham
Title Commercial Loan Originator
Office (800) 641-2905 x68
Direct (240) 617-2435
Email brightleaf4you@mailpost.example

Name Derek Fallow
Office (800) 641-2905 x70
Direct (410) 932-1864
Email d.falthebroker@mailpost.example

Name Gordon Wexley
Office (800) 641-2905 x71
Direct (215) 346-2081
Email g.wexley37@mailpost.example

Name Lyn Moreau
Office (800) 641-2905 x
Direct (202) 458-1937
Email lmoreau64@mailpost.example

Name Nadia Strand
Office (800) 641-2905 x72
Direct (240) 871-5246
Email qrzhomelending@mailpost.example

```html
<!DOCTYPE html>
<html lang="en">
<head>
<meta charset="utf-8">
<title>Commercial Loan Originator Business Cards</title>
<link rel="stylesheet" href="https://fonts.googleapis.com/css2?family=Arimo:wght@400;700&display=swap">
<style>
  :root {
    --backdrop: #666666;
    --orange: #ff8610;
    --cream: #ffffcc;
    --charcoal: #2e2e2e;
    --ring-light: #e6e6e6;
    --white: #ffffff;
  }
  * { margin: 0; padding: 0; box-sizing: border-box; }
  html, body { width: 1200px; height: 1200px; overflow: hidden; }
  body {
    background: var(--backdrop);
    font-family: "Arimo", Arial, sans-serif;
    position: relative;
  }
  .card {
    position: absolute;
    left: 237px;
    width: 726px;
    height: 415px;
    overflow: hidden;
    color: var(--charcoal);
  }
  .card--orange { top: 145px; background: var(--orange); }
  .card--cream { top: 639px; background: var(--cream); }

  .corner-block { position: absolute; background: var(--charcoal); }
  .corner-block--top { right: 0; top: 0; width: 79px; height: 78px; }
  .corner-block--left { left: 0; top: 308px; width: 86px; height: 107px; }
  .base-band { position: absolute; left: 0; bottom: 0; width: 100%; height: 37px; background: var(--charcoal); }

  .pattern-area { position: absolute; }
  .pattern-area--top { left: 43px; top: 42px; width: 142px; height: 118px; }
  .pattern-area--bottom { left: 528px; top: 308px; width: 142px; height: 48px; }
  .card--orange .pattern-area--top { background: linear-gradient(135deg, rgba(255,255,255,0.35), rgba(255,255,255,0.12)); }
  .card--orange .pattern-area--bottom { background: linear-gradient(90deg, rgba(46,46,46,0.3), rgba(46,46,46,0.15)); }
  .card--cream .pattern-area { background: linear-gradient(135deg, rgba(255,134,16,0.4), rgba(255,134,16,0.15)); }

  .portrait {
    position: absolute;
    width: 188px;
    height: 188px;
    border-radius: 50%;
    border: 6px solid var(--ring-light);
  }
  .card--orange .portrait {
    left: 72px; top: 93px;
    background: radial-gradient(circle at 50% 40%, #5a4436 0%, #3a4a63 45%, #1f2a44 100%);
  }
  .card--cream .portrait {
    left: 50px; top: 106px;
    border-color: var(--orange);
    background: radial-gradient(circle at 45% 40%, #8a5a42 0%, #6b5a4c 50%, #2f2a28 100%);
  }

  .contact { position: absolute; left: 0; top: 0; width: 100%; height: 100%; }
  .contact__name, .contact__title, .contact__line { position: absolute; line-height: 1; white-space: nowrap; }
  .contact__name { font-size: 28px; font-weight: 700; text-transform: uppercase; }
  .contact__title { font-size: 14px; letter-spacing: 1px; text-transform: uppercase; }
  .contact__line { font-size: 25px; display: flex; align-items: center; }
  .contact__icon { width: 30px; display: inline-flex; align-items: center; }

  .card--orange .contact__name { left: 292px; top: 102px; letter-spacing: 2.5px; }
  .card--orange .contact__title { left: 292px; top: 138px; }
  .card--orange .contact__line { left: 292px; }
  .card--orange .line-office { top: 176px; }
  .card--orange .line-direct { top: 217px; }
  .card--orange .line-email { top: 255px; }

  .card--cream .contact__name { left: 270px; top: 108px; }
  .card--cream .contact__title { left: 270px; top: 145px; }
  .card--cream .contact__line { left: 270px; }
  .card--cream .line-office { top: 180px; }
  .card--cream .line-direct { top: 220px; }
  .card--cream .line-email { top: 255px; }
</style>
</head>
<body>

<section class="card card--orange">
  <div class="corner-block corner-block--top"></div>
  <div class="corner-block corner-block--left"></div>
  <div class="base-band"></div>

  <div class="pattern-area pattern-area--top" role="img" aria-label="Decorative square dot pattern"></div>
  <div class="pattern-area pattern-area--bottom" role="img" aria-label="Decorative square dot pattern"></div>

  <div class="portrait" role="img" aria-label="Portrait photo of Gordon Wexley in a suit"></div>

  <div class="contact">
    <h1 class="contact__name">Gordon Wexley</h1>
    <p class="contact__title">Commercial Loan Originator</p>
    <p class="contact__line line-office">
      <span class="contact__icon"><svg width="16" height="16" viewBox="0 0 24 24" fill="var(--charcoal)"><path d="M6.6 10.8a15.1 15.1 0 0 0 6.6 6.6l2.2-2.2a1 1 0 0 1 1-.25 11.4 11.4 0 0 0 3.6.57 1 1 0 0 1 1 1V20a1 1 0 0 1-1 1A17 17 0 0 1 3 4a1 1 0 0 1 1-1h3.5a1 1 0 0 1 1 1c0 1.25.2 2.45.57 3.57a1 1 0 0 1-.25 1z"/></svg></span>(800) 641-2905 x71
    </p>
    <p class="contact__line line-direct">
      <span class="contact__icon"><svg width="14" height="20" viewBox="0 0 14 20" fill="none" stroke="var(--charcoal)" stroke-width="1.6"><rect x="1.5" y="1" width="11" height="18" rx="1.5"/><line x1="5" y1="16" x2="9" y2="16"/></svg></span>(215) 346-2081
    </p>
    <p class="contact__line line-email">
      <span class="contact__icon"><svg width="16" height="12" viewBox="0 0 16 12" fill="none" stroke="var(--charcoal)" stroke-width="1.4"><rect x="1" y="1" width="14" height="10"/><path d="M1 1l7 6 7-6"/></svg></span>g.wexley37@mailpost.example
    </p>
  </div>
</section>

<section class="card card--cream">
  <div class="corner-block corner-block--top"></div>
  <div class="corner-block corner-block--left"></div>
  <div class="base-band"></div>

  <div class="pattern-area pattern-area--top" role="img" aria-label="Decorative square dot pattern"></div>
  <div class="pattern-area pattern-area--bottom" role="img" aria-label="Decorative square dot pattern"></div>

  <div class="portrait" role="img" aria-label="Portrait photo of Nadia Strand"></div>

  <div class="contact">
    <h1 class="contact__name">Nadia Strand</h1>
    <p class="contact__title">Commercial Loan Originator</p>
    <p class="contact__line line-office">
      <span class="contact__icon"><svg width="16" height="16" viewBox="0 0 24 24" fill="var(--charcoal)"><path d="M6.6 10.8a15.1 15.1 0 0 0 6.6 6.6l2.2-2.2a1 1 0 0 1 1-.25 11.4 11.4 0 0 0 3.6.57 1 1 0 0 1 1 1V20a1 1 0 0 1-1 1A17 17 0 0 1 3 4a1 1 0 0 1 1-1h3.5a1 1 0 0 1 1 1c0 1.25.2 2.45.57 3.57a1 1 0 0 1-.25 1z"/></svg></span>(800) 641-2905 x72
    </p>
    <p class="contact__line line-direct">
      <span class="contact__icon"><svg width="14" height="20" viewBox="0 0 14 20" fill="none" stroke="var(--charcoal)" stroke-width="1.6"><rect x="1.5" y="1" width="11" height="18" rx="1.5"/><line x1="5" y1="16" x2="9" y2="16"/></svg></span>(240) 871-5246
    </p>
    <p class="contact__line line-email">
      <span class="contact__icon"><svg width="16" height="12" viewBox="0 0 16 12" fill="none" stroke="var(--charcoal)" stroke-width="1.4"><rect x="1" y="1" width="14" height="10"/><path d="M1 1l7 6 7-6"/></svg></span>qrzhomelending@mailpost.example
    </p>
  </div>
</section>

</body>
</html>
```